Independent manufacturing consultant needs a professional Logo & biz card Update

I want a new logo using the existing one as inspiration. The company legal name is Corvex Industrial Trade & Advisory Partners, Inc. Often the name is shortened to Corvex ITP and that matches with web address of www.corvex-itp.example. #1 create a new logo and #2 update biz card. I will need vector file to get cards printed (bilingual English & Japanese). The reverse side will be an exact copy of the original design but in Japanese. I have another resource for the translation so that is not in this scope.
Next month, a follow-up project will be to update the website using new logo and get a professional, cohesive look to all the pages.
Check out web site to get an idea of what we do. The desire is to project professional, articulate, clean, dependable, detailed oriented team of experts.

Target Market(s)

Food and Beverage manufactures. Major players, regiona, and start ups.

Industry/Entity Type

It Company

Contact Information for Business Card

exisiting card and logo provided as foundation but ready to improve upon both!

Logo Text

Corvex ITP or other....

Font styles to use
Sans Serif

Colors
9bcb3c
0356a4

Requirements
Must have
• Logo and biz card.
• Logo will be used for other materials and website.
Nice to have
• open to suggestions.
• Like the Green & Blue colors but also dig grey scale as the website incorporates.
• Open to suggestions.
Should not have
• not to animated. I work with more conservative clients.

```html
<!DOCTYPE html>
<html lang="en">
<head>
<meta charset="utf-8">
<title>Corvex ITP – Business Cards</title>
<link href="https://fonts.googleapis.com/css2?family=Montserrat:wght@600;700&family=Roboto:wght@400;500&display=swap" rel="stylesheet">
<style>
  :root {
    --brand-blue: #0356a4;
    --mid-blue: #1a7fc4;
    --brand-green: #9bcb3c;
    --ink: #1d1d1d;
    --card-white: #ffffff;
    --backdrop: #e8e6e2;
  }
  html, body {
    margin: 0;
    width: 1200px;
    height: 902px;
    overflow: hidden;
    background: var(--backdrop);
  }
  .stage { position: relative; width: 1200px; height: 902px; }
  .card {
    position: absolute;
    width: 600px;
    height: 343px;
    background: var(--card-white);
    box-shadow: 0 6px 18px rgba(0,0,0,0.18);
    overflow: hidden;
  }
  .card-front { left: 80px; top: 70px; }
  .card-back { left: 520px; top: 480px; }

  .front-mark {
    position: absolute;
    left: 0; right: 0; top: 118px;
    text-align: center;
  }
  .wordmark {
    font-family: "Montserrat", sans-serif;
    font-weight: 700;
    color: var(--brand-blue);
    margin: 0;
    line-height: 1;
  }
  .front-mark .wordmark { font-size: 64px; letter-spacing: 1px; }
  .tagline {
    font-family: "Roboto", sans-serif;
    font-weight: 500;
    color: var(--ink);
    text-transform: uppercase;
    margin: 0;
  }
  .front-mark .tagline { font-size: 15px; margin-top: 12px; letter-spacing: 0.5px; }

  .accent-rule {
    position: absolute;
    left: 0; right: 0; bottom: 54px;
    height: 6px;
    background: var(--brand-green);
  }
  .footer-band {
    position: absolute;
    left: 0; right: 0; bottom: 0;
    height: 48px;
    background: var(--brand-blue);
  }

  .back-mark { position: absolute; left: 44px; top: 44px; }
  .back-mark .wordmark { font-size: 38px; }
  .back-mark .tagline { font-size: 9px; margin-top: 6px; letter-spacing: 0.3px; }

  .holder { position: absolute; left: 44px; top: 150px; }
  .holder-name {
    font-family: "Montserrat", sans-serif;
    font-weight: 600;
    font-size: 18px;
    color: var(--brand-blue);
    margin: 0;
    text-transform: uppercase;
    letter-spacing: 0.5px;
  }
  .holder-role {
    font-family: "Roboto", sans-serif;
    font-size: 14px;
    color: var(--brand-green);
    margin: 4px 0 0;
  }

  .contact-list {
    position: absolute;
    left: 330px; top: 146px;
    list-style: none; margin: 0; padding: 0;
    font-family: "Roboto", sans-serif;
    font-size: 17px;
    color: var(--ink);
  }
  .contact-list li { display: flex; align-items: center; gap: 10px; margin-bottom: 10px; }
  .contact-icon {
    width: 20px; height: 20px;
    background: var(--mid-blue);
    border-radius: 3px;
    display: flex; align-items: center; justify-content: center;
    flex: none;
  }
</style>
</head>
<body>
<main class="stage">

  <section class="card card-front" aria-label="Business card front">
    <div class="front-mark">
      <p class="wordmark">Corvex ITP</p>
      <p class="tagline">Industrial Trade &amp; Advisory Partners</p>
    </div>
  </section>

  <section class="card card-back" aria-label="Business card back">
    <div class="back-mark">
      <p class="wordmark">Corvex ITP</p>
      <p class="tagline">Industrial Trade &amp; Advisory Partners</p>
    </div>

    <div class="holder">
      <p class="holder-name">Reid Calloway</p>
      <p class="holder-role">Principal</p>
    </div>

    <ul class="contact-list">
      <li>
        <span class="contact-icon">
          <svg width="12" height="12" viewBox="0 0 24 24" aria-hidden="true"><path fill="#fff" d="M6.6 10.8a15 15 0 0 0 6.6 6.6l2.2-2.2a1 1 0 0 1 1-.25 11.4 11.4 0 0 0 3.6.57 1 1 0 0 1 1 1V20a1 1 0 0 1-1 1A17 17 0 0 1 3 4a1 1 0 0 1 1-1h3.5a1 1 0 0 1 1 1c0 1.25.2 2.45.57 3.57a1 1 0 0 1-.25 1z"/></svg>
        </span>
        555.014.2290
      </li>
      <li>
        <span class="contact-icon">
          <svg width="12" height="12" viewBox="0 0 24 24" aria-hidden="true"><circle cx="12" cy="12" r="9" fill="none" stroke="#fff" stroke-width="2"/><path d="M3 12h18M12 3c3 3 3 15 0 18M12 3c-3 3-3 15 0 18" fill="none" stroke="#fff" stroke-width="1.6"/></svg>
        </span>
        corvex-itp.example
      </li>
      <li>
        <span class="contact-icon">
          <svg width="12" height="12" viewBox="0 0 24 24" aria-hidden="true"><rect x="3" y="5" width="18" height="14" fill="none" stroke="#fff" stroke-width="2"/><path d="M3 6l9 7 9-7" fill="none" stroke="#fff" stroke-width="2"/></svg>
        </span>
        reid@corvex-itp.example
      </li>
    </ul>

    <div class="accent-rule" aria-hidden="true"></div>
    <div class="footer-band" aria-hidden="true"></div>
  </section>

</main>
</body>
</html>
```